House-share and Room Rental Website (With Focus on the Bedroom Landing Page)

Looking for website design for our House-share (executive accommodation) and room rental business.

Our company name is: Lodvenra could also be written as LodVenra or lodvenra. Either is fine .. just looking for a nice clean catchy logo to go with the design.

EXAMPLES
These are examples of other websites in this field that are doing well. this is a kind of baseline.
https://kelbrin.com.au/
https://www.tuvaplex.com/
https://www.nestorvi.com/
https://www.quillsa.net/
https://www.pendlebarrow.com.au/

Our business model is to rent rooms to people looking for high-quality accommodation. We fill the gap between those looking to rent rooms and those with rooms to rent. However, our model is slightly different from those already on the market as we looking to fill a massive gap in the market delivering upmarket rooms for rent.(Executive Accommodation) also in the back end will be coupled with a self management process in the back end.

We offer executive style accommodation that stands out above the rest. With special extras like fire safety.. and management processes that create happier homes. We are looking for a web design package that can help us grow and scale our business. We need a design that is captivating

Our MAIN focus is having a room landing page that stands out from the rest... The core of our business will rely on the promotion of the rooms in a share house... so the whole design relies on the BEDROOM landing page to drive results.

Target Market(s)

We have 2 markets we are aiming at ... the first market is people offering rooms to rent who want the highest rental return. The second market is people looking to rent safe, high-quality rooms, in houses that are well managed and looked after.

Industry/Entity Type

Share Economy

Logo Text

LodVenra

Number of Pages Required

5+ page

Font styles to use
Sans Serif

Colors
3276b5

Requirements
Must have
• A messaging system whereby we can create direct communication between those offering rooms and those looking for rooms.
• A call to action that says " Schedule an Inspection"
• Landing page for promoting rooms
• A home page for showing stock.
• Profile page for those selling rooms
• Profile page for those looking for rooms.
• A scheduling calendar for booking inspections
Nice to have
• Pages where new residents can lock in a room.. pay bond and rents.. and sign contracts
• Notifications
• SMS capabilities in the backend.
Should not have
• No script or handwriting fonts.

```html
<!DOCTYPE html>
<html lang="en">
<head>
<meta charset="utf-8">
<title>Lodvenra – Bedroom</title>
<link href="https://fonts.googleapis.com/css2?family=Barlow:wght@400;500;600&display=swap" rel="stylesheet">
<style>
:root{
  --brand:#3276b5;
  --ink:#222;
  --text:#444;
  --muted:#555;
  --panel:#f0f0f0;
  --rule:#d6d6d6;
  --white:#fff;
}
*{box-sizing:border-box;margin:0;padding:0}
html,body{width:836px;height:1200px;overflow:hidden;background:var(--white)}
body{position:relative;font-family:'Barlow',sans-serif;color:var(--text)}
.abs{position:absolute}

/* header */
.site-header{position:absolute;left:0;top:0;width:836px;height:51px;border-bottom:2px solid #c9c9c9;box-shadow:0 2px 3px rgba(0,0,0,.12)}
.brand{position:absolute;left:120px;top:14px;font-size:18px;color:var(--brand);font-weight:400;letter-spacing:.2px}
.nav a{position:absolute;top:22px;font-size:10.5px;color:var(--text);text-decoration:none}
.cta{position:absolute;left:602px;top:16px;width:113px;height:24px;border:1.2px solid #333;border-radius:12px;font-size:8.5px;font-weight:500;color:var(--ink);display:flex;align-items:center;justify-content:center}

/* room hero */
.room-hero{position:absolute;left:0;top:53px;width:836px;height:507px;background:var(--panel)}
.photo-main{position:absolute;left:0;top:45px;width:516px;height:292px;background:linear-gradient(135deg,#d9d3c5,#a99f8e 55%,#7f7566)}
.thumb{position:absolute;width:70px;height:60px}
.room-title{position:absolute;left:538px;top:42px;font-size:21px;font-weight:400;color:var(--ink);letter-spacing:.5px}
.specs{position:absolute;left:538px;top:76px;width:165px}
.spec{height:27.2px;border-bottom:1px solid var(--rule);display:flex;align-items:center;font-size:10.2px;position:relative;width:165px}
.spec:last-child{border-bottom:none}
.spec .k{color:var(--ink);font-weight:500;width:94px}
.spec .v{color:var(--muted);white-space:nowrap}
.addr-title{position:absolute;left:538px;top:365px;font-size:13px;color:var(--ink);display:flex;align-items:center;gap:3px}
.addr{position:absolute;left:538px;top:387px;font-size:8.8px;line-height:15px;color:var(--text)}
.price{position:absolute;left:539px;top:428px;font-size:13.5px;color:var(--ink)}
.price-v{position:absolute;left:632px;top:427px;font-size:13.5px;color:var(--brand);font-weight:600}
.util{position:absolute;left:539px;top:455px;font-size:10.2px;color:var(--ink);font-weight:500}
.util-v{position:absolute;left:632px;top:455px;font-size:10.2px;color:var(--muted)}

/* amenities */
.sec-title{position:absolute;top:600px;font-size:13px;color:var(--ink)}
.amenity{position:absolute;display:flex;align-items:center;gap:6px;font-size:9px;color:var(--ink);line-height:11px}
.amenity svg{flex:none}
.transport{position:absolute;left:396px;top:642px;font-size:9px;color:var(--ink);display:flex;align-items:center;gap:10px}
.distance{position:absolute;left:396px;top:680px;font-size:9px;color:var(--ink)}
.map{position:absolute;left:396px;top:703px;width:319px;height:162px;background:linear-gradient(120deg,#e6e9e3,#d3e6cc 50%,#e4e6e0)}

/* footer */
.footer-rule{position:absolute;left:0;top:927px;width:836px;border-top:1px solid #ccc}
.foot-brand{position:absolute;left:120px;top:949px;font-size:18px;color:var(--ink)}
.social{position:absolute;top:952px;width:18px;height:18px;border-radius:50%}
.rule{position:absolute;left:120px;width:595px;border-top:1px solid var(--rule)}
.foot-col{position:absolute;top:1006px}
.foot-col h4{font-size:10.5px;font-weight:500;color:var(--ink);margin-bottom:10px}
.foot-col li{list-style:none;font-size:7.6px;line-height:13.1px;color:var(--text)}
.copy{position:absolute;left:0;width:836px;top:1165px;text-align:center;font-size:8px;color:var(--ink)}
</style>
</head>
<body>

<header class="site-header">
  <div class="brand">Lodvenra</div>
  <nav class="nav">
    <a style="left:349px">Home</a>
    <a style="left:398px">About</a>
    <a style="left:449px">Rooms</a>
    <a style="left:503px">News</a>
    <a style="left:551px">Contact</a>
  </nav>
  <div class="cta">Schedule an Inspection</div>
</header>

<section class="room-hero">
  <div class="photo-main" role="img" aria-label="Bedroom with upholstered bed, bench and bedside lamps"></div>

  <div class="thumb" style="left:0;top:341px;background:#8a8d92" role="img" aria-label="Open-plan living space"></div>
  <div class="thumb" style="left:74px;top:341px;background:#c9b58e" role="img" aria-label="Towels and flower"></div>
  <div class="thumb" style="left:149px;top:341px;background:#9e9388" role="img" aria-label="Dining chairs"></div>
  <div class="thumb" style="left:224px;top:341px;background:#8c6a48" role="img" aria-label="Lounge with lamp"></div>
  <div class="thumb" style="left:298px;top:341px;background:#c2b8a8" role="img" aria-label="Clothes rail"></div>
  <div class="thumb" style="left:372px;top:341px;background:#cfd2d4" role="img" aria-label="Kitchen tap"></div>
  <div class="thumb" style="left:446px;top:341px;background:#6e645b" role="img" aria-label="Kitchen"></div>

  <div class="thumb" style="left:0;top:407px;background:#a8885c" role="img" aria-label="Dining area with plant wall"></div>
  <div class="thumb" style="left:74px;top:407px;background:#6f9ec4" role="img" aria-label="Shower head"></div>
  <div class="thumb" style="left:149px;top:407px;background:#7c4f2c" role="img" aria-label="Timber storage stairs"></div>
  <div class="thumb" style="left:224px;top:407px;background:#5c5853" role="img" aria-label="Television unit"></div>
  <div class="thumb" style="left:298px;top:407px;background:#4b5563" role="img" aria-label="Living room sofa"></div>
  <div class="thumb" style="left:372px;top:407px;background:#6b4a2e" role="img" aria-label="Walk-in wardrobe"></div>
  <div class="thumb" style="left:446px;top:407px;background:#9aa1a3" role="img" aria-label="Bathroom"></div>

  <h1 class="room-title">BEDROOM NAME</h1>
  <div class="specs">
    <div class="spec"><span class="k">Gender Preference</span><span class="v">: Male</span></div>
    <div class="spec"><span class="k">Size of room</span><span class="v">: 1200Sqm</span></div>
    <div class="spec"><span class="k">Bathroom</span><span class="v">: Private</span></div>
    <div class="spec"><span class="k">Parking</span><span class="v">: Private</span></div>
    <div class="spec"><span class="k">Smoking</span><span class="v">: Male</span></div>
    <div class="spec"><span class="k">Minimum contract</span><span class="v">: Usually 3 months</span></div>
    <div class="spec"><span class="k">Bed size</span><span class="v">: 12X12</span></div>
    <div class="spec"><span class="k">Type of housemates</span><span class="v">: Professionals</span></div>
    <div class="spec"><span class="k">Room type</span><span class="v">: Private</span></div>
    <div class="spec"><span class="k">Internet speed</span><span class="v">: 180 kbps</span></div>
  </div>

  <div class="addr-title">
    <svg width="8" height="11" viewBox="0 0 8 11"><path d="M4 0.5a3.5 3.5 0 0 0-3.5 3.5C0.5 6.8 4 10.5 4 10.5S7.5 6.8 7.5 4A3.5 3.5 0 0 0 4 0.5z" fill="#333"/><circle cx="4" cy="4" r="1.3" fill="#f0f0f0"/></svg>
    Adress
  </div>
  <div class="addr">Lorem isom 48 Harlow Circle<br>Marden, TX.75014 dummy</div>
  <div class="price">Rental price</div>
  <div class="price-v">: $250.00</div>
  <div class="util">Utilities</div>
  <div class="util-v">: Included</div>
</section>

<section class="amenities">
  <h2 class="sec-title" style="left:120px;font-weight:400">ROOM Amenities</h2>
  <h2 class="sec-title" style="left:396px;font-weight:400">Public amenities..</h2>

  <div class="amenity" style="left:120px;top:641px">
    <svg width="27" height="27" viewBox="0 0 27 27"><rect x=".5" y=".5" width="26" height="26" fill="none" stroke="#777"/><rect x="9" y="5" width="9" height="7" fill="none" stroke="var(--brand)"/><path d="M7 14h13M13.5 14v5M9 22h9M13.5 19v3" stroke="var(--brand)" fill="none"/></svg>
    <span>Furnished/<br>unfurnished</span>
  </div>
  <div class="amenity" style="left:251px;top:641px">
    <svg width="27" height="27" viewBox="0 0 27 27"><rect x=".5" y=".5" width="26" height="26" fill="none" stroke="#777"/><rect x="5" y="7" width="17" height="11" fill="none" stroke="var(--brand)"/><path d="M11 21h5M13.5 18v3" stroke="var(--brand)"/></svg>
    <span>TV</span>
  </div>
  <div class="amenity" style="left:120px;top:683px">
    <svg width="27" height="27" viewBox="0 0 27 27"><rect x=".5" y=".5" width="26" height="26" fill="none" stroke="#777"/><path d="M4 14h19M6 14v8M21 14v8M13 14v6h8" stroke="var(--brand)" fill="none"/><rect x="8" y="7" width="6" height="5" fill="none" stroke="var(--brand)"/></svg>
    <span>Study Desk /<br>&nbsp;Workstation</span>
  </div>
  <div class="amenity" style="left:251px;top:683px">
    <svg width="27" height="27" viewBox="0 0 27 27"><rect x=".5" y=".5" width="26" height="26" fill="none" stroke="#777"/><rect x="5" y="4" width="17" height="19" fill="none" stroke="var(--brand)"/><path d="M13.5 4v19M7 9h4M16 9h4" stroke="var(--brand)"/></svg>
    <span>Wardrobe</span>
  </div>
  <div class="amenity" style="left:120px;top:725px">
    <svg width="27" height="27" viewBox="0 0 27 27"><rect x=".5" y=".5" width="26" height="26" fill="none" stroke="#777"/><rect x="4" y="7" width="19" height="13" fill="none" stroke="var(--brand)"/><path d="M4 11.5h19M4 16h19" stroke="var(--brand)"/></svg>
    <span>Storage space</span>
  </div>
  <div class="amenity" style="left:251px;top:725px">
    <svg width="27" height="27" viewBox="0 0 27 27"><rect x=".5" y=".5" width="26" height="26" fill="none" stroke="#777"/><path d="M20 4v6h-6M8 14a6 4 0 0 1 12 0z" stroke="var(--brand)" fill="none"/><path d="M9 17v2M12 17v3M15 17v2M18 17v3" stroke="var(--brand)"/></svg>
    <span>Ensuite shower</span>
  </div>
  <div class="amenity" style="left:120px;top:766px">
    <svg width="27" height="27" viewBox="0 0 27 27"><rect x=".5" y=".5" width="26" height="26" fill="none" stroke="#777"/><path d="M6 21L20 7M21 21L7 7M18 5l4 4" stroke="var(--brand)" fill="none"/></svg>
    <span>Kitchenette</span>
  </div>

  <div class="transport">
    <span>Transport Options</span>
    <svg width="76" height="22" viewBox="0 0 76 22" fill="none" stroke="#8a8a8a">
      <rect x="2" y="2" width="17" height="16" rx="3"/><path d="M2 10h17M6 22l2-4M15 22l-2-4"/>
      <rect x="29" y="2" width="15" height="17" rx="2"/><path d="M29 9h15M32 21v-2M41 21v-2"/>
      <path d="M54 14v-5l4-5h12l4 5v5z" stroke="var(--brand)"/><circle cx="58" cy="15" r="2" stroke="var(--brand)"/><circle cx="70" cy="15" r="2" stroke="var(--brand)"/>
    </svg>
  </div>
  <div class="distance">Location or distance to the city- 120 km</div>
  <div class="map" role="img" aria-label="Map showing route to the room location"></div>
</section>

<footer>
  <div class="footer-rule"></div>
  <div class="foot-brand">Lodvenra</div>
  <span class="social" style="left:633px;background:#3b5998"></span>
  <span class="social" style="left:654px;background:#29a9e1"></span>
  <span class="social" style="left:675px;background:#0a66a8"></span>
  <span class="social" style="left:696px;background:#e53935"></span>
  <div class="rule" style="top:990px"></div>

  <div class="foot-col" style="left:120px">
    <h4>Room amenities</h4>
    <ul><li>Furnished/unfurnished</li><li>TV</li><li>Storage space</li><li>Study Desk / Workstation</li><li>Wardrobe</li><li>Ensuite shower</li><li>Kitchenette</li></ul>
  </div>
  <div class="foot-col" style="left:306px">
    <h4>Rooms</h4>
    <ul><li>Lorem ipsum dolo</li><li>Consectetur adipiscing elit.</li><li>Fusce eget leo tincid</li><li>Donec consequat</li><li>Praesent elementum</li><li>Jmauris posueret</li><li>Aenean a ex eu lectu</li></ul>
  </div>
  <div class="foot-col" style="left:452px">
    <h4>&nbsp;</h4>
    <ul><li>Lorem ipsum dolo</li><li>Consectetur adipiscing elit.</li><li>Fusce eget leo tincid</li><li>Donec consequat</li><li>Praesent elementum</li><li>Jmauris posueret</li><li>Aenean a ex eu lectu</li></ul>
  </div>
  <div class="foot-col" style="left:616px">
    <h4>Other Links</h4>
    <ul><li>Lorem ipsum dolo</li><li>Consectetur adipiscing elit.</li><li>Fusce eget leo tincid</li><li>Donec consequat</li><li>Praesent elementum</li><li>Jmauris posueret</li><li>Aenean a ex eu lectu</li></ul>
  </div>

  <div class="rule" style="top:1146px"></div>
  <div class="copy">Copyright 2019 Lodvenra. All Rights Reserved</div>
</footer>

</body>
</html>
```